Eyecatching Carpentry Business card

I need a business card designed for myself, my company name is Lewis Dunmore Carpentry.
I am based on the south coast of England and I do all aspects of carpentry, including;
skirting
Architraves
kitchens
roof construction
flooring
doors
loft conversions
decking
windows
I currently have no company logo or letter head so I leave all design ideas to designers.
All I ask is that it looks professional and modern.
A logo may be incorporated as well.
My contact details should be on the back, telephone and email.

```html
<!DOCTYPE html>
<html lang="en">
<head>
<meta charset="utf-8">
<title>Lewis Dunmore Carpentry – Business Card</title>
<link rel="stylesheet" href="https://fonts.googleapis.com/css2?family=Gochi+Hand&family=Josefin+Sans:wght@700&family=Open+Sans:wght@400;600&display=swap">
<style>
  :root {
    --page: #e9e6e2;
    --ink: #0b0b0b;
    --brand-red: #e2352b;
    --gold: #f7b21b;
    --gold-deep: #e38a12;
    --yellow: #ffe81f;
    --white: #ffffff;
    --grey: #9a9a9a;
  }
  html, body {
    margin: 0;
    width: 1200px;
    height: 1200px;
    overflow: hidden;
    background: var(--page);
  }
  .canvas { position: relative; width: 1200px; height: 1200px; }
  .card {
    position: absolute;
    left: 150px;
    width: 900px;
    height: 514px;
    overflow: hidden;
    background: var(--ink);
    box-shadow: 0 10px 30px rgba(0,0,0,.25);
  }
  .card--services { top: 70px; }
  .card--contact { top: 624px; }
  .card__art { position: absolute; inset: 0; width: 100%; height: 100%; }

  /* Services side */
  .services {
    position: absolute;
    left: 48px;
    top: 34px;
    font-family: "Gochi Hand", cursive;
  }
  .services__title {
    margin: 0 0 14px;
    font-size: 34px;
    font-weight: 400;
    color: var(--yellow);
  }
  .services__list { list-style: none; margin: 0; padding: 0 0 0 22px; }
  .services__item {
    display: flex;
    align-items: center;
    gap: 12px;
    font-size: 31px;
    line-height: 40px;
    color: var(--white);
  }
  .services__bullet { width: 14px; height: 14px; flex: none; }

  /* Brand lockup */
  .brand {
    position: absolute;
    display: flex;
    flex-direction: column;
    align-items: center;
    text-align: center;
    font-family: "Josefin Sans", sans-serif;
    font-weight: 700;
    text-transform: uppercase;
  }
  .brand__dot { border-radius: 50%; }
  .brand__main {
    margin: 0;
    white-space: nowrap;
    letter-spacing: 2px;
    line-height: 1;
  }
  .brand__sub {
    display: flex;
    align-items: center;
    gap: 14px;
    width: 100%;
    margin: 8px 0 0;
    white-space: nowrap;
    letter-spacing: 2px;
    line-height: 1;
  }
  .brand__sub::before,
  .brand__sub::after {
    content: "";
    flex: 1;
    height: 2px;
    background: currentColor;
  }

  .card--services .brand { left: 545px; top: 95px; width: 340px; color: var(--white); }
  .card--services .brand__dot { width: 120px; height: 120px; background: var(--white); margin-bottom: 24px; }
  .card--services .brand__main { font-size: 33px; }
  .card--services .brand__sub { font-size: 24px; }

  /* Contact side */
  .card--contact .brand { left: 370px; top: 30px; width: 470px; color: var(--brand-red); }
  .card--contact .brand__dot {
    width: 110px; height: 110px;
    background: radial-gradient(circle, var(--gold) 55%, var(--gold-deep) 100%);
    margin-bottom: 20px;
  }
  .card--contact .brand__main { font-size: 42px; }
  .card--contact .brand__sub { font-size: 32px; }

  .contact {
    position: absolute;
    left: 345px;
    top: 282px;
    width: 520px;
    text-align: center;
    font-family: "Open Sans", sans-serif;
    color: var(--white);
  }
  .contact__name { margin: 0; font-size: 28px; font-weight: 600; letter-spacing: 1px; line-height: 36px; }
  .contact__role { margin: 0 0 14px; font-size: 19px; color: var(--grey); letter-spacing: 1px; line-height: 26px; }
  .contact__line { margin: 0; font-size: 23px; line-height: 40px; letter-spacing: .5px; white-space: nowrap; }
</style>
</head>
<body>
<main class="canvas">

  <section class="card card--services" aria-label="Business card, services side">
    <svg class="card__art" viewBox="0 0 900 514" preserveAspectRatio="none">
      <defs>
        <linearGradient id="woodPanel" x1="0" y1="0" x2="1" y2="1">
          <stop offset="0" stop-color="#b52a12"/>
          <stop offset=".45" stop-color="#e2561f"/>
          <stop offset=".75" stop-color="#f08a3c"/>
          <stop offset="1" stop-color="#c23a16"/>
        </linearGradient>
      </defs>
      <polygon points="590,0 900,0 900,514 440,514" fill="url(#woodPanel)" role="img" aria-label="Polished red timber planks"/>
    </svg>

    <div class="services">
      <h2 class="services__title">I do all aspects of carpentry</h2>
      <ul class="services__list">
        <li class="services__item"><svg class="services__bullet" viewBox="0 0 14 14"><g fill="#fff"><circle cx="7" cy="2" r="2"/><circle cx="7" cy="12" r="2"/><circle cx="2" cy="7" r="2"/><circle cx="12" cy="7" r="2"/></g></svg>Skirting</li>
        <li class="services__item"><svg class="services__bullet" viewBox="0 0 14 14"><g fill="#fff"><circle cx="7" cy="2" r="2"/><circle cx="7" cy="12" r="2"/><circle cx="2" cy="7" r="2"/><circle cx="12" cy="7" r="2"/></g></svg>Architraves</li>
        <li class="services__item"><svg class="services__bullet" viewBox="0 0 14 14"><g fill="#fff"><circle cx="7" cy="2" r="2"/><circle cx="7" cy="12" r="2"/><circle cx="2" cy="7" r="2"/><circle cx="12" cy="7" r="2"/></g></svg>Kitchens</li>
        <li class="services__item"><svg class="services__bullet" viewBox="0 0 14 14"><g fill="#fff"><circle cx="7" cy="2" r="2"/><circle cx="7" cy="12" r="2"/><circle cx="2" cy="7" r="2"/><circle cx="12" cy="7" r="2"/></g></svg>Roof construction</li>
        <li class="services__item"><svg class="services__bullet" viewBox="0 0 14 14"><g fill="#fff"><circle cx="7" cy="2" r="2"/><circle cx="7" cy="12" r="2"/><circle cx="2" cy="7" r="2"/><circle cx="12" cy="7" r="2"/></g></svg>Flooring</li>
        <li class="services__item"><svg class="services__bullet" viewBox="0 0 14 14"><g fill="#fff"><circle cx="7" cy="2" r="2"/><circle cx="7" cy="12" r="2"/><circle cx="2" cy="7" r="2"/><circle cx="12" cy="7" r="2"/></g></svg>Doors</li>
        <li class="services__item"><svg class="services__bullet" viewBox="0 0 14 14"><g fill="#fff"><circle cx="7" cy="2" r="2"/><circle cx="7" cy="12" r="2"/><circle cx="2" cy="7" r="2"/><circle cx="12" cy="7" r="2"/></g></svg>Loft conversions</li>
        <li class="services__item"><svg class="services__bullet" viewBox="0 0 14 14"><g fill="#fff"><circle cx="7" cy="2" r="2"/><circle cx="7" cy="12" r="2"/><circle cx="2" cy="7" r="2"/><circle cx="12" cy="7" r="2"/></g></svg>Decking</li>
        <li class="services__item"><svg class="services__bullet" viewBox="0 0 14 14"><g fill="#fff"><circle cx="7" cy="2" r="2"/><circle cx="7" cy="12" r="2"/><circle cx="2" cy="7" r="2"/><circle cx="12" cy="7" r="2"/></g></svg>Windows</li>
      </ul>
    </div>

    <div class="brand">
      <div class="brand__dot"></div>
      <p class="brand__main">Lewis Dunmore</p>
      <p class="brand__sub">Carpentry</p>
    </div>
  </section>

  <section class="card card--contact" aria-label="Business card, contact side">
    <svg class="card__art" viewBox="0 0 900 514" preserveAspectRatio="none">
      <defs>
        <linearGradient id="woodCurve" x1="0" y1="0" x2="1" y2="1">
          <stop offset="0" stop-color="#a3200f"/>
          <stop offset=".5" stop-color="#e04a1c"/>
          <stop offset="1" stop-color="#f06a2a"/>
        </linearGradient>
        <radialGradient id="toolShade" cx=".55" cy=".5" r=".6">
          <stop offset="0" stop-color="#3a3a3a"/>
          <stop offset="1" stop-color="#0b0b0b"/>
        </radialGradient>
      </defs>
      <rect x="0" y="0" width="900" height="514" fill="url(#toolShade)" role="img" aria-label="Dim photograph of carpentry tools"/>
      <path d="M0 0 H420 Q210 210 110 514 H0 Z" fill="url(#woodCurve)" role="img" aria-label="Curved band of red timber grain"/>
    </svg>

    <div class="brand">
      <div class="brand__dot"></div>
      <p class="brand__main">Lewis Dunmore</p>
      <p class="brand__sub">Carpentry</p>
    </div>

    <div class="contact">
      <p class="contact__name">Lewis Dunmore</p>
      <p class="contact__role">Carpenter</p>
      <p class="contact__line">Phone No : 07700 900412</p>
      <p class="contact__line">Email : info@dunmorejoinery.co.uk</p>
    </div>
  </section>

</main>
</body>
</html>
```